brikMOSA corporation pty ltd

Contruction industry
It's a wall and floor tiling business

Industry/Entity Type

Business

Requirements
Must have
• Likes-
- clean and easy to read
- a witty design is always well received
- for it to look reputable in the industry
- a strong and direct presentation
- simple but striking colour selection
Should not have
• Dislikes-
- pls no tacky square tiles to resemble tiling

```html
<!DOCTYPE html>
<html lang="en">
<head>
<meta charset="utf-8">
<title>brikMOSA corporation pty ltd – Business Card</title>
<link rel="stylesheet" href="https://fonts.googleapis.com/css2?family=Arimo:wght@400;700&display=swap">
<style>
  :root {
    --orange-light: #f7b321;
    --orange: #f29a12;
    --orange-deep: #ea870c;
    --ink: #1c1c1c;
    --muted: #555555;
    --paper: #ffffff;
    --paper-shade: #f1f1f1;
    --divider: #c9c9c9;
    --backdrop: #e7e4df;
  }
  * { margin: 0; padding: 0; box-sizing: border-box; }
  html, body {
    width: 1200px;
    height: 1023px;
    overflow: hidden;
    background: var(--backdrop);
    font-family: "Arimo", Arial, sans-serif;
  }
  .canvas {
    width: 1200px;
    height: 1023px;
    display: flex;
    flex-direction: column;
    align-items: center;
    justify-content: center;
    gap: 56px;
  }
  .card {
    width: 700px;
    height: 428px;
    position: relative;
    overflow: hidden;
    box-shadow: 0 6px 22px rgba(0,0,0,0.14);
  }

  /* Front */
  .card-front {
    background: linear-gradient(120deg, var(--orange-light) 0%, var(--orange) 55%, var(--orange-deep) 100%);
    color: var(--paper);
  }
  .card-front .brand {
    position: absolute;
    left: 0; right: 0;
    top: 138px;
    text-align: center;
  }
  .brand-name {
    font-weight: 700;
    line-height: 1;
    letter-spacing: -1px;
  }
  .card-front .brand-name { font-size: 84px; }
  .brand-sub {
    font-weight: 700;
    letter-spacing: 0.5px;
  }
  .card-front .brand-sub {
    font-size: 19px;
    margin-top: 4px;
    padding-left: 190px;
  }
  .card-front .web {
    position: absolute;
    left: 0; right: 0;
    top: 318px;
    text-align: center;
    font-size: 15px;
    letter-spacing: 3px;
  }

  /* Back */
  .card-back {
    background: linear-gradient(180deg, var(--paper) 0%, var(--paper-shade) 100%);
  }
  .card-back .band {
    position: absolute;
    left: 0; right: 0; bottom: 0;
    height: 52px;
    background: linear-gradient(90deg, var(--orange-light), var(--orange-deep));
  }
  .card-back .brand {
    position: absolute;
    left: 52px;
    top: 150px;
    color: var(--ink);
  }
  .card-back .brand-name { font-size: 62px; }
  .card-back .brand-sub {
    font-size: 14px;
    margin-top: 4px;
    padding-left: 130px;
  }
  .card-back .divider {
    position: absolute;
    left: 392px;
    top: 72px;
    width: 1px;
    height: 228px;
    background: var(--divider);
  }
  .contact {
    position: absolute;
    left: 420px;
    top: 86px;
    color: var(--ink);
  }
  .contact .name {
    font-size: 21px;
    font-weight: 400;
    letter-spacing: 0.3px;
  }
  .contact .role {
    font-size: 14px;
    color: var(--muted);
    margin-top: 6px;
  }
  .contact ul {
    list-style: none;
    margin-top: 26px;
  }
  .contact li {
    display: flex;
    align-items: center;
    gap: 10px;
    font-size: 16px;
    margin-bottom: 8px;
  }
  .contact svg { width: 15px; height: 15px; flex: none; }
  .icon { fill: none; stroke: var(--orange-deep); stroke-width: 1.8; stroke-linecap: round; stroke-linejoin: round; }
</style>
</head>
<body>
<main class="canvas">
  <section class="card card-front" aria-label="Card front">
    <div class="brand">
      <div class="brand-name">brikMOSA</div>
      <div class="brand-sub">corporation pty ltd</div>
    </div>
    <div class="web">www.brikmosa.com</div>
  </section>

  <section class="card card-back" aria-label="Card back">
    <div class="brand">
      <div class="brand-name">brikMOSA</div>
      <div class="brand-sub">corporation pty ltd</div>
    </div>
    <div class="divider"></div>
    <div class="contact">
      <div class="name">DAN MARLOW</div>
      <div class="role">Director</div>
      <ul>
        <li>
          <svg viewBox="0 0 16 16" aria-hidden="true"><path class="icon" d="M4 2 L6.5 5 L5 6.8 C6 9 7 10 9.2 11 L11 9.5 L14 12 L12.5 14 C7 13.5 2.5 9 2 3.5 Z"/></svg>
          <span>0400 555 018</span>
        </li>
        <li>
          <svg viewBox="0 0 16 16" aria-hidden="true"><rect class="icon" x="1.5" y="3.5" width="13" height="9"/><path class="icon" d="M1.5 3.5 L8 9 L14.5 3.5"/></svg>
          <span>dan.marlow@mail.com</span>
        </li>
        <li>
          <svg viewBox="0 0 16 16" aria-hidden="true"><circle class="icon" cx="8" cy="8" r="6.3"/><ellipse class="icon" cx="8" cy="8" rx="2.8" ry="6.3"/><path class="icon" d="M1.7 8 H14.3"/></svg>
          <span>www.brikmosa.com</span>
        </li>
      </ul>
    </div>
    <div class="band"></div>
  </section>
</main>
</body>
</html>
```